Book Cover - The Velvet Lantern Almanac Collection

We are writing a book about the velvet lantern almanac collection, including Guerrilla Marketing. Advertising, Branding and PR.

We are looking for a fun and quirky cover, and are open to your ideas 💡
My website and social media are on www.TorvanPelica.co and posts are shared on Trelvano. Again we are open to ideas

```html
<!DOCTYPE html>
<html lang="en">
<head>
<meta charset="UTF-8">
<title>The Velvet Lantern Almanac Collection — Book Cover</title>
<link rel="stylesheet" href="https://fonts.googleapis.com/css2?family=Bebas+Neue&display=swap">
<style>
  :root {
    --page: #ffffff;
    --cover-yellow: #fff200;
    --ink: #0d0d0d;
    --band-red: #d7202a;
    --band-blue: #22409a;
    --photo-light: #f3f3f0;
    --photo-mid: #b9b6ae;
    --photo-warm: #e9c96a;
  }
  * { margin: 0; padding: 0; box-sizing: border-box; }
  html, body {
    width: 1200px;
    height: 1200px;
    overflow: hidden;
    background: var(--page);
  }
  .book-cover {
    position: absolute;
    left: 360px;
    top: 240px;
    width: 480px;
    height: 720px;
    background: var(--cover-yellow);
    overflow: hidden;
    font-family: "Bebas Neue", "Oswald", sans-serif;
  }
  .collage {
    position: absolute;
  }
  .collage--idea {
    left: 248px;
    top: 18px;
    width: 184px;
    height: 232px;
    border-radius: 92px 92px 12px 12px;
    background: radial-gradient(circle at 45% 38%, var(--photo-warm) 0%, var(--photo-light) 42%, var(--photo-mid) 100%);
  }
  .collage--chatter {
    left: 232px;
    top: 410px;
    width: 240px;
    height: 300px;
    border-radius: 120px 60px 90px 140px;
    background: linear-gradient(160deg, var(--photo-light) 0%, #dcdcd8 55%, var(--photo-mid) 100%);
  }
  .cover-title {
    position: absolute;
    inset: 0;
    font-weight: 400;
    font-size: 118px;
    line-height: 1;
    text-transform: uppercase;
  }
  .title-line {
    position: absolute;
    left: 0;
    height: 116px;
    display: flex;
    align-items: center;
  }
  .word {
    height: 100%;
    display: flex;
    align-items: center;
    padding: 8px 10px 0 10px;
    letter-spacing: 1px;
  }
  .word--plain { color: var(--ink); }
  .word--red { background: var(--band-red); color: var(--cover-yellow); }
  .word--blue { background: var(--band-blue); color: var(--cover-yellow); }
  .line-1 { top: 12px; }
  .line-2 { top: 129px; }
  .line-3 { top: 249px; gap: 4px; right: 0; }
  .line-3 .word--blue { flex: 1; }
  .line-4 { top: 369px; }
  .line-5 { top: 492px; }
  .line-6 { top: 606px; }
</style>
</head>
<body>
  <main class="book-cover">
    <div class="collage collage--idea" role="img" aria-label="Collage of a man in glasses holding a glowing light bulb and gears, raised on a hand"></div>
    <div class="collage collage--chatter" role="img" aria-label="Collage of an open mouth sending a ribbon of blah blah text into a large ear"></div>

    <h1 class="cover-title" aria-label="The Velvet Lantern Almanac Collection">
      <span class="title-line line-1"><span class="word word--plain">The</span></span>
      <span class="title-line line-2"><span class="word word--red">Velvet</span></span>
      <span class="title-line line-3"><span class="word word--red">Lan</span><span class="word word--blue">tern</span></span>
      <span class="title-line line-4"><span class="word word--blue">Almanac</span></span>
      <span class="title-line line-5"><span class="word word--plain">Collec</span></span>
      <span class="title-line line-6"><span class="word word--plain">tion</span></span>
    </h1>
  </main>
</body>
</html>
```